Boutique custom software development company needs new business card

Our nearly 20 year old custom software development company would like to better include the fact that we are now providing Bitcoin services. These new services are B2B include education (how to acquire and securely hold Bitcoin) and integrating Bitcoin payments into existing ecommerce sites or other existing systems. Please keep the card clean and simple. Attached is our current design and some other files. vexalon.example

Target Market(s)

businesses owners interested in long term relationship

Industry/Entity Type

Custom software development and Bitcoin

Contact Information for Business Card

Marcus Ellwood, marcus@vexalon.example, vexalon.example, (888) 555-VEXAL

Font styles to use
Other font styles liked:
• monospace

Requirements
Must have
• double-sided
Nice to have
• clean and simple
Should not have
• physical address

```html
<!DOCTYPE html>
<html lang="en">
<head>
<meta charset="utf-8">
<title>Vexalon Business Card</title>
<link rel="stylesheet" href="https://fonts.googleapis.com/css2?family=Lato:wght@300&family=Montserrat:wght@500;600;700;800&display=swap">
<style>
  :root {
    --stage: #3a322e;
    --card: #232323;
    --card-edge: #1a1a1a;
    --orange: #ef8a2f;
    --blue: #4f86cc;
    --white: #f2f2f2;
    --emboss: #5a5a5a;
    --emboss-tag: #4a4a4a;
  }
  * { box-sizing: border-box; margin: 0; padding: 0; }
  html, body {
    width: 1200px; height: 716px; overflow: hidden;
    background: var(--stage);
  }
  .canvas {
    width: 1200px; height: 716px;
    display: flex; align-items: center; justify-content: center; gap: 48px;
  }
  .card {
    width: 540px; height: 309px;
    background: linear-gradient(160deg, #2c2c2c 0%, var(--card) 55%, var(--card-edge) 100%);
    border-radius: 6px;
    box-shadow: 0 14px 30px rgba(0,0,0,.45);
    position: relative;
  }
  .card--front {
    display: flex; flex-direction: column; align-items: center; justify-content: center;
    border-bottom: 4px solid var(--orange);
  }
  .front-name {
    font-family: "Montserrat", sans-serif; font-weight: 800;
    font-size: 66px; letter-spacing: 1px; color: var(--emboss); line-height: 1;
  }
  .front-tagline {
    font-family: "Lato", sans-serif; font-weight: 300;
    font-size: 21px; color: var(--emboss-tag); margin-top: 6px;
  }
  .card--back { display: flex; align-items: center; padding: 0 24px 0 30px; }
  .brand { width: 262px; }
  .brand-name {
    font-family: "Montserrat", sans-serif; font-weight: 800;
    font-size: 42px; color: var(--blue); line-height: 1; letter-spacing: .5px;
  }
  .brand-tagline {
    font-family: "Lato", sans-serif; font-weight: 300;
    font-size: 14px; color: var(--blue); margin-top: 5px; white-space: nowrap;
  }
  .divider { width: 1.5px; height: 130px; background: var(--orange); margin: 0 20px 0 12px; flex: none; }
  .contact { font-family: "Montserrat", sans-serif; font-weight: 500; color: var(--white); font-size: 13px; line-height: 1.55; }
  .contact-name { font-weight: 700; font-size: 18px; letter-spacing: .5px; line-height: 1.2; white-space: nowrap; }
  .contact-name .first { color: var(--orange); }
  .contact-name .last { color: var(--blue); }
  .contact-title { font-size: 13px; letter-spacing: .5px; margin-bottom: 8px; }
  .contact-row { display: flex; align-items: center; gap: 6px; white-space: nowrap; }
  .contact-row svg { width: 10px; height: 10px; flex: none; }
  .web-accent { color: var(--orange); }
  .web-domain { color: var(--blue); }
</style>
</head>
<body>
<main class="canvas">
  <section class="card card--front" aria-label="Card front">
    <div class="front-name">VEXALON</div>
    <div class="front-tagline">custom applications &amp; bitcoin services</div>
  </section>

  <section class="card card--back" aria-label="Card back">
    <div class="brand">
      <div class="brand-name">VEXALON</div>
      <div class="brand-tagline">custom applications &amp; bitcoin services</div>
    </div>
    <div class="divider"></div>
    <div class="contact">
      <div class="contact-name"><span class="first">MARCUS</span> <span class="last">ELLWOOD</span></div>
      <div class="contact-title">DIRECTOR</div>
      <div class="contact-row">
        <svg viewBox="0 0 10 10" aria-hidden="true"><path d="M2 1 L4 1 L4.5 3 L3.3 3.8 Q4.3 5.8 6.2 6.7 L7 5.5 L9 6 L9 8 Q5 9 1.5 5 Q1 3 2 1 Z" fill="var(--orange)"/></svg>
        <span>(888) 555-VEXAL</span>
      </div>
      <div class="contact-row">
        <svg viewBox="0 0 10 10" aria-hidden="true"><rect x="1" y="2.5" width="8" height="5.5" fill="none" stroke="var(--orange)" stroke-width="1"/><path d="M1 2.5 L5 5.5 L9 2.5" fill="none" stroke="var(--orange)" stroke-width="1"/></svg>
        <span>marcus@vexalon.example</span>
      </div>
      <div class="contact-row">
        <svg viewBox="0 0 10 10" aria-hidden="true"><circle cx="5" cy="5" r="4" fill="none" stroke="var(--orange)" stroke-width="1"/><ellipse cx="5" cy="5" rx="1.8" ry="4" fill="none" stroke="var(--orange)" stroke-width=".8"/><line x1="1" y1="5" x2="9" y2="5" stroke="var(--orange)" stroke-width=".8"/></svg>
        <span>www.<span class="web-accent">vexalon</span><span class="web-domain">.example</span></span>
      </div>
    </div>
  </section>
</main>
</body>
</html>
```